Dietetic office: Bright Plate

I want to give my business card a modern and warm look (which attracts the eye and has a reassuring side), which links dietetics to a moment of well-being. The front and back sides must be used (not just to put the logo on the front side)

The map should be eye-catching and easy to read. I don't necessarily want to have a plain background, which I find visually weighs down the maps.
I really like the square format of a business card with rounded edges which is different from what we are used to finding (and why not take this square diagonally?), however I am not closed to another format as long as I like the style.

Who am I? Mireille, 32 years old, Dietician and passionate about food since always. I am specialized in slimming and an expert in micro nutrition, which means that I take into account not only the nutritional balance while maintaining pleasure (if foods are present in the business card, I do not want some cliché things where there would just be fruits and vegetables, but really something more global), but also the psycho-emotional dimension that I will treat with food supplements based on plants, fruits or vegetables.

-----------------------------------------------------------------------------------

 Mention to appear on the card IN FRENCH (please be careful in case of translation that the use of words is correct):

Mireille DORAN
Dietician Nutritionist
Expert in Slimming and Micro-Nutrition

Slogan: I help you lose weight sustainably with pleasure and by reconciling your events

Catchphrases: Want to lose weight? Do you like going out? Do you have a lot of events? And is pleasure on your plate important to you?

Make an appointment on Rendiplan or on 06 41 58 30 92
mireille.brightplate@exemplo-mail.fr
Address: Health Center, Rue des Glycines, 13127 Vitrolles
www.brightplate-exemple.fr
Friendwall + Picturo Logo

- The company logo has been uploaded for your viewing. Other file formats can be made available if required.
- I would like a place for a photo of me to be possible.

Good morning,
I want to have a business card that is both lively and warm. Which will easily catch the eye while being easy to read and make people understand that I am in the field of well-being.
I like the square side in business cards (and why not use them diagonally?), or a more classic but original one.
Both the front and back sides must be used (I don't want to have the logo on just one side)
I don't want to have a plain background, but rather something more muted (I really like the suggestion from "Reed Cloud Graphic Designer" for this)
the use of logo for telephone, mail, address, rendiplan, friendwall, pictu etc is possible in order to facilitate reading

Please follow the various elements of the brief regarding the text and use the French text as it is.

I like business cards preferably square (with the possibility of using them diagonally).
The map should be eye-catching and easy to read.
It must bring pep while having softness which brings back to the well-being side
The card must be used on the front and back for the different elements (I do not want to have only the logo on the front side)
The text must correspond to the brief (be careful with the translation which can sometimes be bad)
I don't want to have a plain blue or orange background. I really like the idea of the background from "Reed Cloud Graphic Designer"

You can if you wish use symbols for contacts, telephone, rendiplan, address, fw, pictu....

Target Market(s)

mainly women between 25 and 65 years old + men around 40 years old

Contact Information for Business Card

Font styles to use
Sans Serif
Script

Colors
0054AA
0677BA
7BADD7
CADEEF
E8F1F8
0094D4
00A9DD
6FCCEA
C7EBF8
E9F6FB
00AB8E
00BBA5
67D7C9
C6EFE9
E9F9F6
FFC000
F8CF3A
FAE287
FDF2CF
FEFAEE
F0912C
F2A743
F7CA91
FBE8D2
FDF5EE

Requirements
Must have
• some pep! while being refined
Nice to have
• I really like the square format of a business card with rounded edges which is different from what we are used to finding, however I am not closed to another format as long as I like the style.
Should not have
• if foods are represented, only show fruits and vegetables (too cliché)

```html
<!DOCTYPE html>
<html lang="fr">
<head>
<meta charset="utf-8">
<title>Bright Plate – carte de visite</title>
<link href="https://fonts.googleapis.com/css2?family=Allura&family=Gelasio:wght@400&family=Marcellus&family=Montserrat:wght@600;700&family=Open+Sans:wght@400;700&display=swap" rel="stylesheet">
<style>
  :root {
    --canvas: #979797;
    --ink: #111111;
    --blue: #0677ba;
    --bright-blue: #0a6cf0;
    --red: #e23b2e;
    --back-bg: #e5f8fb;
    --photo-light: #cfe6ec;
    --photo-mid: #a9cfd9;
    --photo-slot: #cccccc;
    --white: #ffffff;
    --orange: #f0912c;
  }
  * { margin: 0; padding: 0; box-sizing: border-box; }
  html, body { width: 1200px; height: 1000px; overflow: hidden; }
  body { background: var(--canvas); position: relative; }

  .card {
    position: absolute;
    top: 268px;
    width: 520px;
    height: 518px;
    border-radius: 40px;
    overflow: hidden;
  }
  .card--front { left: 70px; }
  .card--back { left: 620px; background: var(--back-bg); }

  .food-photo {
    position: absolute; inset: 0;
    background:
      radial-gradient(circle at 18% 22%, #c9a07a 0, #7f8a55 26%, transparent 36%),
      radial-gradient(circle at 8% 82%, #d47b55 0, #9bb364 18%, transparent 26%),
      linear-gradient(135deg, var(--photo-mid), var(--photo-light) 55%, #dbeef2);
  }

  .wave { position: absolute; left: 0; bottom: 0; width: 520px; height: 518px; }

  .front-hook {
    position: absolute; left: 0; width: 520px;
    font-family: "Marcellus", serif;
    color: var(--ink);
  }
  .front-hook__line { position: absolute; font-size: 36px; line-height: 1; white-space: nowrap; }
  .front-hook__line--1 { left: 212px; top: 192px; }
  .front-hook__line--2 { left: 227px; top: 228px; }
  .front-hook__accent {
    position: absolute; left: 136px; top: 246px;
    font-family: "Allura", cursive;
    font-size: 118px; line-height: 1;
    color: var(--bright-blue);
  }
  .front-hook__end {
    position: absolute; left: 184px; top: 352px;
    font-family: "Marcellus", serif;
    font-size: 26px; color: var(--red); white-space: nowrap;
  }

  .brand {
    position: absolute; right: 36px; bottom: 40px;
    font-family: "Open Sans", sans-serif;
    font-size: 27px; font-weight: 400;
    color: var(--blue);
    display: flex; align-items: center; gap: 8px;
  }
  .brand__dot { width: 12px; height: 12px; border-radius: 50%; background: var(--orange); }

  .slogan {
    position: absolute; left: 50px; top: 44px;
    font-family: "Gelasio", serif;
    font-size: 27px; line-height: 36px; color: var(--ink);
  }
  .person { position: absolute; left: 51px; top: 210px; font-family: "Open Sans", sans-serif; }
  .person__name { font-family: "Montserrat", sans-serif; font-weight: 700; font-size: 22px; color: var(--bright-blue); }
  .person__role { font-size: 14.5px; line-height: 22px; color: var(--ink); margin-top: 4px; }

  .contact { position: absolute; left: 51px; top: 325px; font-family: "Open Sans", sans-serif; }
  .contact__booking { font-family: "Montserrat", sans-serif; font-weight: 700; font-size: 13px; line-height: 17px; color: var(--bright-blue); }
  .contact__phone { font-weight: 700; font-size: 32px; color: var(--ink); line-height: 1; margin-top: 13px; }
  .contact__mail { font-size: 14.5px; color: var(--ink); margin-top: 6px; }
  .contact__web { font-size: 19px; color: var(--bright-blue); margin-top: 20px; }
  .contact__web strong { font-weight: 700; }
  .social { display: flex; gap: 4px; margin-top: 4px; }
  .social__item { width: 22px; height: 22px; border-radius: 50%; }
  .social__item--friendwall { background: var(--bright-blue); }
  .social__item--picturo { background: var(--orange); }

  .portrait-slot {
    position: absolute; left: 308px; top: 181px;
    width: 174px; height: 174px; border-radius: 50%;
    background: var(--photo-slot);
  }
</style>
</head>
<body>

  <section class="card card--front">
    <div class="food-photo" role="img" aria-label="Photo vue de dessus d'assiettes de salade colorée sur fond bleu clair"></div>
    <svg class="wave" viewBox="0 0 520 518" aria-hidden="true">
      <path d="M0 518 C150 470 260 395 400 400 C470 402 505 412 520 422 L520 518 Z" fill="#ffffff"/>
    </svg>
    <div class="front-hook">
      <span class="front-hook__line front-hook__line--1">Et le plaisir</span>
      <span class="front-hook__line front-hook__line--2">dans votre</span>
      <span class="front-hook__accent">assiette</span>
      <span class="front-hook__end">est important pour vous?</span>
    </div>
    <div class="brand"><span class="brand__dot"></span>Bright Plate</div>
  </section>

  <section class="card card--back">
    <svg class="wave" viewBox="0 0 520 518" aria-hidden="true">
      <path d="M0 518 C150 470 260 395 400 400 C470 402 505 412 520 422 L520 518 Z" fill="#ffffff"/>
    </svg>
    <p class="slogan">Je vous aide à mincir<br>durablement avec plaisir<br>et en conciliant vos<br>évènements</p>
    <div class="person">
      <p class="person__name">Mireille DORAN</p>
      <p class="person__role">Diététicienne Nutritionniste<br>Experte en Amincissement<br>et en Micro-Nutrition</p>
    </div>
    <div class="contact">
      <p class="contact__booking">PRISE DE RENDEZ-VOUS<br>SUR RENDIPLAN OU AU</p>
      <p class="contact__phone">06 41 58 30 92</p>
      <p class="contact__mail">mireille.brightplate@exemplo-mail.fr</p>
      <p class="contact__web"><strong>brightplate-exemple</strong>.fr</p>
      <div class="social">
        <span class="social__item social__item--friendwall" aria-label="Friendwall"></span>
        <span class="social__item social__item--picturo" aria-label="Picturo"></span>
      </div>
    </div>
    <div class="portrait-slot" role="img" aria-label="Emplacement pour la photo de Mireille"></div>
    <div class="brand"><span class="brand__dot"></span>Bright Plate</div>
  </section>

</body>
</html>
```